Flyer für Indoorspielplatz
Zielgruppe
Hüpfland Ostbahnhof, Indoorspielplatz für Kinder, Ich suche einen Flyer für unserer Eröffnung am 14.12.2024 im ansprechenden (eventuell kindergerechten) Design in der Größe A6, eventuell Doppelseitig wobei auf der Rückseite einige Attraktionen von uns aufgezählt werden sollen eventuell mit Bildern aus dem Web bez. aus dem 3D Plan (nähere Details hierzu kann ich ggf. nachliefern bzw. selbst dann anstelle des Platzhalters ergänzen)
Aufgabenstellung
Der Flyer sollte in DIN A6 Format sein, soll alle wichtigen Punkte wie Name: Hüpfland Ostbahnhof, Neueröffnung, Datum, Indoorspielplatz, Adresse 4720 Lindenau - Amselgrundweg 12 (eventuell mit kleiner Anfahrtsskizze), Logo, ... enthalten und wenn optisch möglich in den Farben unserers Logo gehalten sein. Bildwerkhaus abo ist vorhanden und kann ggf. daher die Bilder übermittelt werden.

```html
<!DOCTYPE html>
<html lang="de">
<head>
<meta charset="utf-8">
<title>Hüpfland Ostbahnhof – Flyer Neueröffnung</title>
<link rel="stylesheet" href="https://fonts.googleapis.com/css2?family=Sniglet:wght@400;800&display=swap">
<style>
  :root {
    --pink: #e8325a;
    --orange: #ef8133;
    --green: #4cae2f;
    --white: #ffffff;
    --ink: #1a1a1a;
    --stage: #4a4a4a;
    --jungle-a: #5cb83a;
    --jungle-b: #a3663a;
    --photo-a: #f5cf3a;
    --photo-b: #e58c4a;
  }
  html, body { margin: 0; padding: 0; }
  body {
    width: 1200px; height: 1200px; overflow: hidden;
    background: var(--stage);
    position: relative;
    font-family: "Sniglet", "Comic Sans MS", sans-serif;
  }
  .flyer {
    position: absolute; top: 268px;
    width: 471px; height: 664px;
    overflow: hidden;
  }
  .flyer--front { left: 102px; background: var(--pink); }
  .flyer--back { left: 627px; background: var(--orange); }
  .flyer__shapes { position: absolute; inset: 0; }

  .front__illustration {
    position: absolute; left: 36px; top: 14px; width: 400px; height: 300px;
    border-radius: 48% 48% 40% 40%;
    background: radial-gradient(circle at 50% 45%, var(--jungle-b) 0 30%, var(--jungle-a) 60%, #3f8f2a 100%);
  }
  .front__name {
    position: absolute; left: 0; width: 420px; top: 318px;
    text-align: center; margin: 0;
    font-weight: 800; font-size: 44px; line-height: 1.0;
    color: var(--pink);
  }
  .front__opening {
    position: absolute; left: 208px; top: 452px; width: 260px;
    transform: rotate(11deg); transform-origin: left top;
    margin: 0; line-height: 1.05; white-space: nowrap;
  }
  .front__opening-name { display: block; font-weight: 800; font-size: 20px; color: var(--ink); }
  .front__opening-label { display: block; font-weight: 800; font-size: 24px; color: var(--pink); margin-top: 2px; }
  .front__opening-date { display: block; font-weight: 800; font-size: 40px; color: var(--green); }

  .back__brand {
    position: absolute; left: 100px; top: 48px; width: 170px; height: 150px;
    display: flex; flex-direction: column; align-items: center; gap: 6px;
  }
  .back__illustration {
    width: 140px; height: 90px; border-radius: 46% 46% 38% 38%;
    background: radial-gradient(circle at 50% 45%, var(--jungle-b) 0 30%, var(--jungle-a) 65%, #3f8f2a 100%);
  }
  .back__name {
    margin: 0; text-align: center; font-weight: 800; font-size: 20px; line-height: 1.05;
    color: var(--pink);
  }
  .back__type {
    position: absolute; left: 59px; top: 206px; margin: 0;
    font-weight: 800; font-size: 24px; color: var(--pink);
  }
  .back__address {
    position: absolute; left: 59px; top: 236px; margin: 0;
    font-weight: 800; font-style: normal; color: var(--green);
    font-size: 17px; line-height: 1.2;
  }
  .back__address-city { display: block; font-size: 21px; margin-top: 6px; }
  .attractions { position: absolute; inset: 0; margin: 0; padding: 0; list-style: none; }
  .attractions__item { position: absolute; font-weight: 800; font-size: 22px; white-space: nowrap; }
  .attractions__item--pink { color: var(--pink); }
  .attractions__item--green { color: var(--green); }
  .back__photo {
    position: absolute; left: -1px; top: 391px; width: 298px; height: 298px;
    border-radius: 50%;
    background: radial-gradient(circle at 42% 45%, #f3c7a8 0 18%, var(--photo-a) 45%, var(--photo-b) 100%);
  }
</style>
</head>
<body>

<section class="flyer flyer--front" aria-label="Vorderseite">
  <svg class="flyer__shapes" width="471" height="664" viewBox="0 0 471 664" aria-hidden="true">
    <ellipse cx="209" cy="161" rx="258" ry="288" fill="#ffffff"/>
    <circle cx="327" cy="533" r="142" fill="#ffffff"/>
  </svg>
  <div class="front__illustration" role="img" aria-label="Dschungel-Illustration mit Baumhaus, Affen, Papagei und Regenbogen"></div>
  <h1 class="front__name">Hüpfland<br>Ostbahnhof</h1>
  <p class="front__opening">
    <span class="front__opening-name">Hüpfland Ostbahnhof</span>
    <span class="front__opening-label">NEUERÖFFNUNG</span>
    <span class="front__opening-date">14.12.2024</span>
  </p>
</section>

<section class="flyer flyer--back" aria-label="Rückseite">
  <svg class="flyer__shapes" width="471" height="664" viewBox="0 0 471 664" aria-hidden="true">
    <circle cx="185" cy="186" r="172" fill="#ffffff"/>
    <circle cx="342" cy="397" r="156" fill="#ffffff"/>
  </svg>
  <div class="back__brand">
    <div class="back__illustration" role="img" aria-label="Kleine Dschungel-Illustration mit Affen und Papagei"></div>
    <p class="back__name">Hüpfland<br>Ostbahnhof</p>
  </div>
  <h2 class="back__type">Indoorspielplatz</h2>
  <address class="back__address">
    Amselgrundweg 12
    <span class="back__address-city">4720 Lindenau</span>
  </address>
  <ul class="attractions">
    <li class="attractions__item attractions__item--pink" style="left:238px;top:310px">Attraktion 1</li>
    <li class="attractions__item attractions__item--green" style="left:250px;top:347px">Attraktion 2</li>
    <li class="attractions__item attractions__item--pink" style="left:268px;top:384px">Attraktion 3</li>
    <li class="attractions__item attractions__item--green" style="left:264px;top:421px">Attraktion 4</li>
  </ul>
  <div class="back__photo" role="img" aria-label="Foto: lachendes Kind auf bunten Spielpolstern im Indoorspielplatz"></div>
</section>

</body>
</html>
```